Visit card

Industry/Entity Type

Health Care

Contact Information for Business Card

O VITAL SYSTEMIQUE
Odile Ferrand - chef de Projet

Requirements
Must have
• 318 Rue des Tilleuls Verts 47150 BÉTHUNE Tel: 33 (0) 487 204 615 Mobile: 06 42 93 17 58 Web: www.cliniqorvane.example Contact: o.ferrand@o-vitalsystemique.example
Should not have
• Respect for color

```html
<!DOCTYPE html>
<html lang="fr">
<head>
<meta charset="utf-8">
<title>O Vital Systemique – Business Card</title>
<link href="https://fonts.googleapis.com/css2?family=Poppins:wght@300;400;600&display=swap" rel="stylesheet">
<style>
  :root {
    --backdrop: #e9e6e3;
    --card-dark: #3e3e40;
    --card-light: #ffffff;
    --ink: #4a4a4c;
    --ink-soft: #6a6a6c;
    --accent: #e3212d;
    --white: #ffffff;
  }
  * { margin: 0; padding: 0; box-sizing: border-box; }
  html, body {
    width: 1200px; height: 1055px; overflow: hidden;
    background: var(--backdrop);
    font-family: "Poppins", sans-serif;
  }
  .stage {
    position: relative; width: 1200px; height: 1055px;
    display: flex; align-items: center; justify-content: center; gap: 50px;
  }
  .card {
    position: relative; width: 540px; height: 320px;
    border-radius: 22px; overflow: hidden;
    border-bottom: 4px solid var(--accent);
    box-shadow: 0 10px 24px rgba(0,0,0,.18);
  }
  /* front */
  .card--front { background: var(--card-dark); }
  .front-brand {
    position: absolute; left: 50px; top: 110px;
    display: flex; align-items: center; gap: 18px;
  }
  .front-brand__dot {
    width: 74px; height: 74px; border-radius: 50%;
    background: var(--white); flex: none;
  }
  .front-brand__name {
    color: var(--white); font-weight: 600; font-size: 27px;
    letter-spacing: 1.5px; line-height: 1;
  }
  .front-web {
    position: absolute; left: 50px; bottom: 60px;
    color: var(--white); font-weight: 300; font-size: 15px; letter-spacing: .3px;
  }
  .front-web .accent { color: var(--accent); }
  /* back */
  .card--back { background: var(--card-light); }
  .back-brand {
    position: absolute; left: 40px; top: 70px; width: 170px;
    display: flex; flex-direction: column; align-items: center; gap: 14px;
  }
  .back-brand__dot {
    width: 130px; height: 130px; border-radius: 50%; background: var(--ink);
  }
  .back-brand__name {
    color: var(--ink); font-weight: 600; font-size: 13px; letter-spacing: 1px;
    text-align: center;
  }
  .divider {
    position: absolute; left: 232px; top: 60px; width: 1px; height: 170px;
    background: var(--ink-soft);
  }
  .details {
    position: absolute; left: 252px; top: 52px; right: 20px;
    color: var(--ink); font-size: 12.5px; line-height: 1.45;
  }
  .details__name {
    color: var(--accent); font-weight: 600; font-size: 19px; letter-spacing: 1px;
    line-height: 1.2;
  }
  .details__role { font-weight: 400; margin-bottom: 4px; }
  .details__address { font-weight: 300; margin-bottom: 10px; }
  .contact-list { list-style: none; }
  .contact-list li {
    display: flex; align-items: center; gap: 8px; font-weight: 300;
    white-space: nowrap;
  }
  .contact-list svg { width: 11px; height: 11px; flex: none; fill: var(--accent); }
</style>
</head>
<body>
<main class="stage">
  <section class="card card--front" aria-label="Card front">
    <div class="front-brand">
      <span class="front-brand__dot"></span>
      <span class="front-brand__name">O VITAL<br>SYSTEMIQUE</span>
    </div>
    <p class="front-web">www.<span class="accent">cliniqorvane</span>.example</p>
  </section>

  <section class="card card--back" aria-label="Card back">
    <div class="back-brand">
      <span class="back-brand__dot"></span>
      <span class="back-brand__name">O VITAL SYSTEMIQUE</span>
    </div>
    <span class="divider"></span>
    <div class="details">
      <h1 class="details__name">ODILE FERRAND</h1>
      <p class="details__role">Chef de Projet</p>
      <p class="details__address">318 Rue des Tilleuls Verts<br>47150 BÉTHUNE</p>
      <ul class="contact-list">
        <li><svg viewBox="0 0 16 16"><path d="M3 1l3 0 1.5 4-2 1.2a9 9 0 0 0 4.3 4.3L11 8.5l4 1.5v3a2 2 0 0 1-2 2A12 12 0 0 1 1 3a2 2 0 0 1 2-2z"/></svg>+33 (0) 487 204 615</li>
        <li><svg viewBox="0 0 16 16"><path d="M4 0h8a1 1 0 0 1 1 1v14a1 1 0 0 1-1 1H4a1 1 0 0 1-1-1V1a1 1 0 0 1 1-1zm1 2v10h6V2zm3 11a1 1 0 1 0 0 2 1 1 0 0 0 0-2z"/></svg>06 42 93 17 58</li>
        <li><svg viewBox="0 0 16 16"><path d="M0 3h16v10H0zm1.5 1.2v.3L8 9l6.5-4.5v-.3z"/></svg>o.ferrand@o-vitalsystemique.example</li>
        <li><svg viewBox="0 0 16 16"><circle cx="8" cy="8" r="8"/></svg>www.cliniqorvane.example</li>
      </ul>
    </div>
  </section>
</main>
</body>
</html>
```